Automotive component supplier needs a business card design

We need a business card design for our company called Vexlo Global Fittings Ltd based in the UK. We are a supplier of interior and exterior components to premium car manufacturers such as Harwick Vale, Denby Stroud, Calloway and Ferrucatti. We would like to see a modern business card design that uses the colour blue.

Target Market(s)

Premium automotive car manufacturers.

Industry/Entity Type

Automotive

Contact Information for Business Card

Company Name : Vexlo Global Fittings Limited
Address: 17 Tamsin Yard, Upper Heath, Warwick, CV32 8LN, United Kingdom
Web Address : www.vexlofittings-demo.co.uk

Font styles to use
Other font styles liked:
• Helvetica

Colors
3176b5
0255a3
85acd3
cfdeed
cee9f5
85cae6
34a6d7
0692cd
9bcb3c

Requirements
Must have
• Clear company logo and a mixture of blue colours.
Nice to have
• A high quality modern image.
Should not have
• Multiple colours.

```html
<!DOCTYPE html>
<html lang="en">
<head>
<meta charset="utf-8">
<title>Vexlo Global Fittings – Business Card</title>
<link href="https://fonts.googleapis.com/css2?family=Roboto:wght@300;400;700&display=swap" rel="stylesheet">
<style>
  :root {
    --bg: #e9edf1;
    --card: #ffffff;
    --blue: #1e9ad6;
    --blue-deep: #0692cd;
    --band-light: #34a6d7;
    --green: #9bcb3c;
    --ink-light: #ffffff;
  }
  * { box-sizing: border-box; margin: 0; padding: 0; }
  html, body { width: 1200px; height: 950px; overflow: hidden; }
  body {
    background: var(--bg);
    font-family: "Roboto", Helvetica, Arial, sans-serif;
    display: flex;
    flex-direction: column;
    align-items: center;
    justify-content: center;
    gap: 50px;
  }
  .card {
    width: 700px;
    height: 400px;
    background: var(--card);
    position: relative;
    overflow: hidden;
    box-shadow: 0 6px 18px rgba(20, 40, 60, 0.18);
  }

  /* Company name lockup: plain text, one colour, one weight */
  .brand { display: flex; flex-direction: column; line-height: 1; color: var(--blue); font-weight: 700; }
  .brand-name { letter-spacing: 2px; }
  .brand-sub { letter-spacing: 2.4px; }

  /* Front */
  .card-front .accent-band { position: absolute; left: 0; top: 0; width: 100%; height: 12px; background: var(--green); }
  .card-front .brand { position: absolute; left: 70px; top: 92px; }
  .card-front .brand-name { font-size: 50px; }
  .card-front .brand-sub { font-size: 12.5px; margin-top: 4px; }
  .person { position: absolute; left: 390px; top: 124px; }
  .person-name { color: var(--blue); font-weight: 700; font-size: 21px; letter-spacing: 0.5px; }
  .person-role { color: var(--green); font-weight: 300; font-size: 17px; margin-top: 4px; }

  .contact-band {
    position: absolute; left: 0; bottom: 0; width: 100%; height: 158px;
    background: linear-gradient(180deg, var(--band-light), var(--blue-deep));
    color: var(--ink-light);
  }
  .contact-list { position: absolute; left: 36px; bottom: 16px; list-style: none; font-size: 15px; font-weight: 300; }
  .contact-list li { display: flex; align-items: center; gap: 10px; height: 24px; white-space: nowrap; }
  .contact-list svg { width: 14px; height: 14px; flex: none; }
  .address { position: absolute; right: 34px; top: 24px; text-align: right; font-size: 16px; font-weight: 300; line-height: 1.45; font-style: normal; }

  /* Back */
  .card-back { display: flex; align-items: center; justify-content: center; }
  .card-back .brand-name { font-size: 104px; letter-spacing: 4px; }
  .card-back .brand-sub { font-size: 24px; margin-top: 8px; letter-spacing: 4.6px; }
</style>
</head>
<body>

  <section class="card card-front" aria-label="Business card front">
    <div class="accent-band"></div>
    <div class="brand">
      <span class="brand-name">VEXLO</span>
      <span class="brand-sub">GLOBAL FITTINGS</span>
    </div>
    <div class="person">
      <p class="person-name">MARCUS ELLERY</p>
      <p class="person-role">CEO / Founder</p>
    </div>
    <div class="contact-band">
      <ul class="contact-list">
        <li>
          <svg viewBox="0 0 24 24" aria-hidden="true"><path fill="#fff" d="M6.6 10.8a15.1 15.1 0 0 0 6.6 6.6l2.2-2.2a1 1 0 0 1 1-.25 11.4 11.4 0 0 0 3.6.57 1 1 0 0 1 1 1V20a1 1 0 0 1-1 1A17 17 0 0 1 3 4a1 1 0 0 1 1-1h3.5a1 1 0 0 1 1 1c0 1.25.2 2.45.57 3.57a1 1 0 0 1-.25 1z"/></svg>
          <span>604 318 7725</span>
        </li>
        <li>
          <svg viewBox="0 0 24 24" aria-hidden="true"><rect x="3" y="3" width="18" height="18" fill="none" stroke="#fff" stroke-width="2.4"/></svg>
          <span>604 318 7790</span>
        </li>
        <li>
          <svg viewBox="0 0 24 24" aria-hidden="true"><rect x="2" y="5" width="20" height="14" fill="#fff"/><path d="M2 5l10 8 10-8" fill="none" stroke="#0692cd" stroke-width="1.8"/></svg>
          <span>marcus@vexlofittings-demo.co.uk</span>
        </li>
        <li>
          <svg viewBox="0 0 24 24" aria-hidden="true"><circle cx="12" cy="12" r="9" fill="none" stroke="#fff" stroke-width="2"/><path d="M3 12h18M12 3c-3 3.5-3 14.5 0 18M12 3c3 3.5 3 14.5 0 18" fill="none" stroke="#fff" stroke-width="1.6"/></svg>
          <span>www.vexlofittings-demo.co.uk</span>
        </li>
      </ul>
      <address class="address">
        17 Tamsin Yard, Upper Heath<br>
        Warwick, CV32 8LN<br>
        United Kingdom
      </address>
    </div>
  </section>

  <section class="card card-back" aria-label="Business card back">
    <div class="brand">
      <span class="brand-name">VEXLO</span>
      <span class="brand-sub">GLOBAL FITTINGS</span>
    </div>
  </section>

</body>
</html>
```